HomeBridle business card and stationary design

We are looking for a simple yet elegant design for our mortgage company business card and stationary.

The card should include:
Name (Derek Walsh)
Title (CEO)
Phone Number (614-208-3917)
Address (48 Birchfield Court, Suite 314, Marlow, OH 43952)
Email (email@homebridle-example.com)
"NMLS" i.e. (NMLS 61947)
"Company NMLS" (Company NMLS 472815)

See above

```html
<!DOCTYPE html>
<html lang="en">
<head>
<meta charset="utf-8">
<title>HomeBridle Business Card</title>
<link rel="stylesheet" href="https://fonts.googleapis.com/css2?family=Poppins:wght@400;500;600&display=swap">
<style>
  :root {
    --navy: #17222e;
    --blue: #29abe2;
    --white: #ffffff;
    --ink: #1a2530;
    --stage: #d8dce1;
  }
  * { margin: 0; padding: 0; box-sizing: border-box; }
  html, body { width: 1200px; height: 900px; overflow: hidden; }
  body {
    background: var(--stage);
    font-family: "Poppins", sans-serif;
    position: relative;
  }
  .card {
    position: absolute;
    left: 260px;
    width: 680px;
    height: 389px;
    border-radius: 22px;
    overflow: hidden;
    box-shadow: 0 6px 18px rgba(0,0,0,0.18);
  }
  .card-back { top: 40px; background: var(--navy); }
  .card-front { top: 471px; background: var(--white); }

  .wordmark {
    font-family: "Poppins", sans-serif;
    font-weight: 500;
    letter-spacing: 1px;
    line-height: 1;
    position: absolute;
  }
  .card-back .wordmark {
    color: var(--blue);
    font-size: 68px;
    left: 0; right: 0; top: 158px;
    text-align: center;
  }
  .card-front .wordmark {
    color: var(--ink);
    font-size: 50px;
    right: 58px; top: 80px;
  }

  .divider {
    position: absolute;
    left: 210px; right: 58px; top: 196px;
    height: 1.5px;
    background: var(--ink);
  }
  .person { position: absolute; left: 58px; top: 160px; }
  .person-name { font-size: 27px; font-weight: 600; color: var(--ink); line-height: 1; }
  .person-title { font-size: 21px; font-weight: 500; color: var(--blue); margin-top: 4px; line-height: 1.1; }

  .contacts { position: absolute; left: 62px; top: 228px; list-style: none; }
  .contacts li {
    display: flex; align-items: center; gap: 14px;
    font-size: 17px; color: var(--ink); line-height: 1; margin-bottom: 12px;
  }
  .contacts svg, .address svg { width: 17px; height: 17px; flex: none; }

  .address {
    position: absolute; right: 58px; top: 218px;
    display: flex; gap: 12px; align-items: flex-start;
    font-size: 15px; color: var(--ink); line-height: 1.35;
  }
  .address svg { margin-top: 8px; }

  .bands { position: absolute; left: 0; top: 0; width: 680px; height: 389px; }
  .nmls-personal {
    position: absolute; left: 72px; bottom: 17px;
    color: var(--white); font-size: 16px; font-weight: 500; letter-spacing: 0.5px; line-height: 1;
  }
  .nmls-company {
    position: absolute; right: 36px; top: 305px;
    color: var(--white); font-size: 16px; font-weight: 500; letter-spacing: 0.5px; line-height: 1;
  }
</style>
</head>
<body>
  <section class="card card-back" aria-label="Card back">
    <div class="wordmark">HomeBridle</div>
  </section>

  <section class="card card-front" aria-label="Card front">
    <svg class="bands" viewBox="0 0 680 389" aria-hidden="true">
      <polygon points="0,335 400,335 358,389 0,389" fill="var(--navy)"/>
      <polygon points="370,389 440,300 680,300 680,389 455,389 508,326 472,326 398,389" fill="var(--blue)"/>
    </svg>

    <div class="wordmark">HomeBridle</div>
    <div class="divider"></div>

    <div class="person">
      <div class="person-name">Derek Walsh</div>
      <div class="person-title">(CEO)</div>
    </div>

    <ul class="contacts">
      <li>
        <svg viewBox="0 0 24 24" aria-hidden="true"><path fill="var(--blue)" d="M6.6 10.8a15.1 15.1 0 0 0 6.6 6.6l2.2-2.2a1 1 0 0 1 1-.25 11.4 11.4 0 0 0 3.6.57 1 1 0 0 1 1 1V20a1 1 0 0 1-1 1A17 17 0 0 1 3 4a1 1 0 0 1 1-1h3.5a1 1 0 0 1 1 1c0 1.25.2 2.45.57 3.57a1 1 0 0 1-.25 1z"/></svg>
        614-208-3917
      </li>
      <li>
        <svg viewBox="0 0 24 24" aria-hidden="true"><rect x="2" y="5" width="20" height="14" fill="var(--blue)"/><path d="M2 5l10 8 10-8M2 19l7-7M22 19l-7-7" stroke="var(--white)" stroke-width="1.5" fill="none"/></svg>
        email@homebridle-example.com
      </li>
    </ul>

    <div class="address">
      <svg viewBox="0 0 24 24" aria-hidden="true"><path fill="var(--blue)" d="M12 2a7 7 0 0 0-7 7c0 5 7 13 7 13s7-8 7-13a7 7 0 0 0-7-7zm0 9.5A2.5 2.5 0 1 1 12 6.5a2.5 2.5 0 0 1 0 5z"/></svg>
      <div>48 Birchfield Court, Suite 314<br>Marlow, OH 43952</div>
    </div>

    <div class="nmls-company">Company NMLS 472815</div>
    <div class="nmls-personal">NMLS 61947</div>
  </section>
</body>
</html>
```